Need A Fresher Look & Feel For Our Water Testing Product

We need one insert design for our at home water testing, we're looking something that pops a bit more than we currently have.

We're looking to show that it's an at-home test that allows you to test for multiple things with one easy to use test. Also the fact it includes double tests for almost everything (except bacteria).
Updates

Low design quality

Target Market(s)

Men and women aged 30-60

Industry/Entity Type

Water Company

Font styles to use
Serif

Colors
33a6d7
85cae6

Requirements
Must have
• This packaging will be a little bit different dimensions, we are going to be using a zippered pouch that has a matte finish. Here's an example of the type of packaging. https://im07.verpogrix.com/kf/QRM4k72nbuXP5TqLWdve8GZRRMsk/Laminated-aluminum-foil-zip-lock-bag-stand.jpg_350x350.jpg
• The dimensions of our pouch will be: 5.75in x 5.5in
• Looking for something clean that really pops, try to use blues because of the water testing aspect. We like to use clean crisp light colors to signify cleanliness and clean water.
• We want some kind of color wheel like we currently have that gives a different color for each of the following tests. It helps make it pop out seeing that 8 different types of tests are included.
• - E. Coli / Bacteria
• - pH
• - Total Alkalinity
• - Total Hardness
• - Total Chlorine
• - Nitrite
• - Nitrate
• - Heavy Metals
• Also maybe make a point the kit includes 2 tests for each of the following: (Only one without 3 is the bacteria)
• - pH
• - Total Alkalinity
• - Total Hardness
• - Total Chlorine
• - Nitritie
• - Nirtate
• - Heavy Metals
• IMPORTANT!
• The blue & white below should be the main colors, but you please choose the 8 colors for the color wheel.
Nice to have
• We have another similar older kit which the packaging is attached for. We want the new one to be much more eye catching the current one.

```html
<!DOCTYPE html>
<html lang="en">
<head>
<meta charset="utf-8">
<title>Complete Water Analysis Test Kit – Pouch Insert</title>
<link rel="stylesheet" href="https://fonts.googleapis.com/css2?family=Open+Sans:wght@700;800&display=swap">
<style>
  :root {
    --blue: #2fa6da;
    --blue-light: #85cae6;
    --ink: #1d1d1d;
    --white: #ffffff;
    --red: #ee2224;
    --orange: #f9a51a;
    --yellow: #e8e41a;
    --green-dark: #1e8a3e;
    --green: #4cb848;
    --sky: #34b2e8;
    --purple: #7a2a8e;
    --magenta: #c2449a;
  }
  * { box-sizing: border-box; margin: 0; padding: 0; }
  html, body { width: 1148px; height: 1200px; overflow: hidden; background: var(--white); }
  body { font-family: "Open Sans", Arial, sans-serif; }

  .insert { position: relative; width: 1148px; height: 1200px; background: var(--white); }

  .title-band {
    position: absolute; left: 0; top: 0; width: 100%; height: 216px;
    background: var(--blue); color: var(--white);
    display: flex; flex-direction: column; justify-content: center; align-items: center;
  }
  .title {
    font-weight: 800; font-size: 74px; line-height: 76px; letter-spacing: 1px;
    text-align: center; text-transform: uppercase;
  }

  .subtitle-band, .tagline-band {
    position: absolute; left: 0; width: 100%;
    background: var(--blue-light); color: var(--ink);
    display: flex; align-items: center; justify-content: center;
    font-weight: 700;
  }
  .subtitle-band { top: 216px; height: 65px; font-size: 25px; }
  .tagline-band { top: 990px; height: 49px; font-size: 23px; }

  .test-wheel { position: absolute; left: 0; top: 281px; width: 1148px; height: 709px; }
  .test-wheel text { font-family: "Open Sans", Arial, sans-serif; }
  .circle-label { fill: var(--white); font-weight: 700; font-size: 25px; }
  .center-count { fill: #000; font-weight: 800; }

  .double-badge {
    position: absolute; left: 853px; top: 344px; width: 295px; height: 86px;
    background: var(--blue); color: var(--white);
    border-radius: 43px 0 0 43px;
    display: flex; flex-direction: column; justify-content: center; align-items: center;
    line-height: 1.1;
  }
  .double-badge .badge-main { font-weight: 800; font-size: 31px; }
  .double-badge .badge-note { font-weight: 800; font-size: 18px; }

  .footer-band { position: absolute; left: 0; top: 1039px; width: 100%; height: 161px; background: var(--blue); }
  .brand-box {
    position: absolute; left: 52px; top: 1068px; width: 467px; height: 94px;
    background: var(--white);
    display: flex; align-items: center; justify-content: center;
  }
  .brand-name { color: var(--blue); font-weight: 800; font-size: 44px; letter-spacing: 1px; text-transform: uppercase; }
  .origin-badge { position: absolute; left: 628px; top: 1090px; width: 86px; height: 60px; background: var(--white); }
  .label-space { position: absolute; left: 816px; top: 1068px; width: 300px; height: 105px; background: var(--white); }
</style>
</head>
<body>
<main class="insert">
  <header class="title-band">
    <h1 class="title">Complete Water<br>Analysis Test Kit</h1>
  </header>

  <p class="subtitle-band">Easy At-Home Testing Kit For Both Well &amp; Municipal Water</p>

  <svg class="test-wheel" viewBox="0 0 1148 709" aria-label="Ten tests included: E. coli and bacteria, pH, total alkalinity, total hardness, total chlorine, nitrite, nitrate and heavy metals">
    <g fill-opacity="0.9">
      <circle cx="580" cy="135" r="103" fill="var(--red)"/>
      <circle cx="740" cy="210" r="103" fill="var(--orange)"/>
      <circle cx="806" cy="353" r="103" fill="var(--yellow)"/>
      <circle cx="740" cy="497" r="103" fill="var(--green-dark)"/>
      <circle cx="580" cy="569" r="103" fill="var(--green)"/>
      <circle cx="422" cy="497" r="103" fill="var(--sky)"/>
      <circle cx="358" cy="353" r="103" fill="var(--purple)"/>
      <circle cx="422" cy="210" r="103" fill="var(--magenta)"/>
    </g>
    <g class="circle-label" text-anchor="middle">
      <text x="580" y="120">E.Coli./</text>
      <text x="580" y="154">Bacteria</text>
      <text x="740" y="220">pH</text>
      <text x="806" y="337">Total</text>
      <text x="806" y="371">Alkalinity</text>
      <text x="740" y="481">Total</text>
      <text x="740" y="515">Hardness</text>
      <text x="580" y="553">Total</text>
      <text x="580" y="587">Chlorine</text>
      <text x="422" y="506">Nitrite</text>
      <text x="358" y="362">Nitrate</text>
      <text x="422" y="194">Heavy</text>
      <text x="422" y="228">Metals</text>
    </g>
    <g class="center-count" text-anchor="middle">
      <text x="580" y="325" font-size="56">10</text>
      <text x="580" y="372" font-size="48">TESTS</text>
      <text x="580" y="403" font-size="25">INCLUDED</text>
    </g>
  </svg>

  <div class="double-badge">
    <span class="badge-main">DOUBLE TEST</span>
    <span class="badge-note">EXCEPT FOR BACTERIA</span>
  </div>

  <p class="tagline-band">Know What You And Your Family Are Drinking!</p>

  <footer class="footer-band"></footer>
  <div class="brand-box"><span class="brand-name">Clearwell Check</span></div>
  <div class="origin-badge" role="img" aria-label="Made in USA badge"></div>
  <div class="label-space"></div>
</main>
</body>
</html>
```